COMPETITION TITLE:
Premium Skincare Packaging Design for Modern Hydration Beauty Brand
ABOUT THE PROJECT
We are developing a new skincare brand called VELORENA.
We are looking for a sophisticated and commercially strong packaging design direction for our initial skincare soft launch.
The brand positioning is:
* modern premium skincare
* hydration-focused
* wellness-oriented
* calming and elegant
* emotionally reassuring
* modern feminine skincare
* premium online beauty brand
The products are designed around hydration, skin comfort and modern skincare rituals.
The brand is inspired by modern hydration and skin wellness for people adapting between warmer and colder climates. The visual direction should therefore feel emotionally warm, comforting and restorative while remaining modern, refined and internationally premium rather than overtly cultural or decorative.
WHAT WE NEED
We are primarily seeking the VISUAL DIRECTION and PACKAGING IDENTITY for one hero product:
LIGHT MOISTURISING DAY CREAM
The winning visual direction will later be adapted across additional products within the range, including:
* Brightening Eye Cream
* Hydrating Mist / Toner
Therefore we are looking for a cohesive skincare brand identity system rather than unrelated individual designs.
IMPORTANT PACKAGING INFORMATION
The product packaging is:
* white plastic pump dispenser bottle
* transparent clear plastic lid
* outer cardboard carton/box
Bottle dimensions:
* diameter: 30mm
* total height including lid: 147mm
* bottle body height: approx. 120mm
* transparent lid height: approx. 27mm
Outer carton dimensions:
* height: 150mm
* width: 40mm x 35mm
IMPORTANT:
The packaging itself is minimalist and lightweight, therefore the LABEL DESIGN and OVERALL BRAND DIRECTION should visually elevate the product and make it feel:
* premium
* substantial
* calming
* elegant
* modern
* trustworthy
* emotionally warm
* intentional
The design should help the packaging feel significantly more premium than standard mass-market skincare.
FILES PROVIDED
We are providing:
* bottle label template
* outer box template
* logo/icon
* packaging dimensions
The supplied logo/icon should be retained conceptually, however designers may professionally refine and recreate/vectorise the artwork where required for packaging consistency and premium presentation.
At this stage we are NOT looking for final technical production artwork.
We are primarily looking for:
* visual direction
* typography
* colour palette
* premium skincare aesthetic
* realistic product mockups
IMPORTANT WEBSITE NOTE
A current website link may be provided for background information only.
Please DO NOT take heavy visual inspiration from the existing website design, as the website itself is expected to evolve in the future alongside the packaging direction.
The packaging design should therefore LEAD the future visual identity of the brand rather than follow the current website styling.
DESIGN STYLE
We are looking for:
* modern premium wellness skincare
* understated luxury
* elegant typography
* emotionally warm but clean branding
* hydration-focused beauty aesthetic
* premium online skincare look
The product should feel:
* calming when held
* emotionally reassuring rather than clinical
* modern wellness rather than minimalist pharmacy
* elegant but human rather than cold luxury
* comforting and restorative rather than cosmetic-only
Subtle texture, tonal layering and sophisticated visual depth are encouraged where appropriate.
Designers are encouraged to create a recognisable and distinctive visual identity rather than generic minimalist skincare packaging.
PLEASE AVOID
* gold luxury clichés
* ornate decorative themes
* floral overload
* influencer-style beauty branding
* overly clinical pharmacy aesthetics
* generic Canva-style layouts
* packaging that feels cold or sterile
STYLE REFERENCES
Please take inspiration from brands such as:
* Mirven
* Plume Beauty
* Coraval
* Beauty of Dallith
We particularly like:
* elegant spacing
* clean premium typography
* calm colour palettes
* subtle luxury
* modern hydration skincare aesthetics
COLOUR DIRECTION
Preferred tones include:
* warm ivory
* soft cream
* muted blush
* sand
* charcoal typography
* subtle deep plum accents
* restrained muted rose-gold accents
Please avoid:
* neon colours
* excessive metallic effects
* harsh black-and-white pharmacy styling
* very dark packaging
IMPORTANT DESIGN NOTE
The slim vertical packaging should feel intentionally elegant and premium rather than small or sample-sized.
The label design should visually elongate and elevate the packaging.
LOGO
An existing logo/icon is provided and should be retained and integrated into the design direction rather than completely redesigned.
DELIVERABLES
We are looking for:
* one fully developed hero product design
* realistic bottle + outer box mockups
* coordinated visual direction suitable for future product extensions
* typography and colour direction
* editable source files
The final approved visual system will later be adapted across additional products within the range.
BRAND NAME
VELORENA
OPTIONAL TAGLINE DIRECTION
Tideshift Balance Hydration
Updates
Thank you everyone for the submissions so far — there are some very strong directions emerging.
A few important thoughts as the project develops:
We are looking not only for attractive skincare labels, but for a distinctive and recognisable BRAND IDENTITY that could grow with the business over time across future packaging formats including larger cartons, jars and premium skincare packaging.
One area we would particularly encourage designers to explore further is refinement/elevation of the existing logo/icon. We would like to retain the core rose/circle concept, however subtle refinement, balance, geometry, typography pairing and premium presentation are encouraged where appropriate.
The strongest directions for us so far are those that feel:
* emotionally warm rather than clinical
* modern premium wellness rather than generic minimal skincare
* calming and reassuring when viewed or held
* elegant and distinctive rather than trend-driven
* premium without relying on gold luxury clichés
We are especially interested in designs that create a memorable visual identity system rather than simply placing text onto a white skincare bottle.
Subtle tonal layering, refined typography, understated sophistication and intelligent visual restraint are all encouraged.
Many thanks again and we are very excited to see the next round of directions develop.

```html
<!DOCTYPE html>
<html lang="en">
<head>
<meta charset="utf-8">
<title>VELORENA – Light Moisturising Day Cream Label</title>
<link rel="stylesheet" href="https://fonts.googleapis.com/css2?family=Montserrat:wght@500&family=Inter:wght@400;500;600&display=swap">
<style>
  :root {
    --backdrop: #f2ddc7;
    --label-sand: #dcc6aa;
    --label-sand-light: #e3cfb4;
    --ink-charcoal: #2e2219;
    --mark-blush: #ecc9bb;
    --mark-ring: #5a4333;
  }
  * { margin: 0; padding: 0; box-sizing: border-box; }
  html, body {
    width: 799px;
    height: 1200px;
    overflow: hidden;
    background: var(--backdrop);
  }
  .canvas {
    position: relative;
    width: 799px;
    height: 1200px;
  }
  .label {
    position: absolute;
    left: 241px;
    top: 60px;
    width: 317px;
    height: 1080px;
    background: linear-gradient(90deg, var(--label-sand) 0%, var(--label-sand-light) 45%, var(--label-sand) 100%);
    color: var(--ink-charcoal);
  }
  .brand-mark {
    position: absolute;
    left: 50%;
    top: 193px;
    transform: translateX(-50%);
    width: 214px;
    height: 214px;
  }
  .brand-name {
    position: absolute;
    top: 418px;
    left: 0;
    width: 100%;
    text-align: center;
    font-family: "Montserrat", sans-serif;
    font-weight: 500;
    font-size: 24px;
    letter-spacing: 0.2em;
    padding-left: 0.2em;
  }
  .product-block {
    position: absolute;
    left: 46px;
    top: 606px;
    font-family: "Inter", sans-serif;
  }
  .product-title {
    font-size: 27px;
    line-height: 34px;
    font-weight: 400;
    text-transform: uppercase;
  }
  .product-title strong {
    display: block;
    font-weight: 600;
  }
  .title-rule {
    width: 150px;
    height: 1px;
    margin: 12px 0 10px;
    background: linear-gradient(90deg, var(--ink-charcoal) 70%, transparent);
  }
  .product-notes {
    font-size: 19px;
    line-height: 29px;
    font-weight: 400;
  }
  .volume {
    position: absolute;
    top: 994px;
    left: 0;
    width: 100%;
    text-align: center;
    font-family: "Inter", sans-serif;
    font-weight: 600;
    font-size: 24px;
    letter-spacing: 0.1em;
  }
</style>
</head>
<body>
  <main class="canvas">
    <section class="label">
      <svg class="brand-mark" viewBox="0 0 214 214" aria-hidden="true">
        <circle cx="107" cy="107" r="105" fill="var(--mark-blush)" stroke="var(--mark-ring)" stroke-width="2"/>
      </svg>
      <p class="brand-name">VELORENA</p>

      <div class="product-block">
        <h1 class="product-title">Light<br>Moisturising<strong>Day Cream</strong></h1>
        <div class="title-rule"></div>
        <p class="product-notes">With Green Tea<br>Normal to Oily Skin</p>
      </div>

      <p class="volume">50ML</p>
    </section>
  </main>
</body>
</html>
```